Werbebanner für Textilreinigung
Zielgruppe
Wir sind eine Textilreinigung mit einem großen Spektrum an Leistungen.
Unsere Zielgruppe sind Privat Personen die ihre Textilien zum reinigen zu uns bringen.
Aufgabenstellung
Es sollen 5 Straßenbanner designt werden. Diese werden bei Ortseinfahrten/- ausfahrten, aufgehängt. Das Design soll modern sein und zu unserem Logo passen. Die Herausforderung bei den Straßenbannern ist die Zielgruppe, die Autofahrer. Der Banner wird beim Vorbeifahren für nur 1-2 Sekunden gesehen. Auf jedem Banner soll ein Sonderangebot mit eingebaut werden. Zu der Zeit in der der Banner aufgehängt ist, erhält der Kunde 20% auf die jeweilige Dienstleistung.
Hier die verschiedenen Banner:
-Betten & Daunenreinigung | -Trachten und Lederreinigung | -Braut & Festtagskleider reinigung |-Teppichwäsche (inkl. kostenlosen Abhol und Lieferservice) |-Hemdenservice
Bannergröße beträgt 100cm(H) x 300cm(B)
Das gilt für alle 5 verschiedenen Banner.
Es soll auf jedem Banner stehen:
-Sonderangebot 20%
-unser Logo (siehe Dateien)
-unsere Adresse
-Telefonnummer
-Aufruf zur Aktion
Anmerkung: Auf der EPS.Datei muss ein kleiner Schriftzug hinzugefügt werden der auf der PDF. zu sehen ist.

```html
<!DOCTYPE html>
<html lang="de">
<head>
<meta charset="utf-8">
<title>FEINWERK – Party alles klar</title>
<link rel="stylesheet" href="https://fonts.googleapis.com/css2?family=Roboto:wght@300;400;500;700&family=Dancing+Script:wght@500&display=swap">
<style>
  :root {
    --brand-blue: #123f94;
    --brand-green: #5bb531;
    --paper: #ffffff;
    --frame: #2a2a2a;
  }
  * { margin: 0; padding: 0; box-sizing: border-box; }
  html, body { width: 1200px; height: 400px; overflow: hidden; background: var(--paper); }
  .banner {
    position: relative;
    width: 1200px;
    height: 400px;
    background: var(--paper);
    border: 1px solid var(--frame);
    font-family: "Roboto", Arial, sans-serif;
    overflow: hidden;
  }
  .photo-child {
    position: absolute;
    left: 760px; top: 0;
    width: 440px; height: 400px;
    background:
      radial-gradient(ellipse 170px 150px at 250px 110px, rgba(214,170,125,0.85) 0%, rgba(214,170,125,0.35) 55%, rgba(214,170,125,0) 100%),
      radial-gradient(ellipse 170px 230px at 250px 330px, rgba(28,33,70,0.95) 0%, rgba(28,33,70,0.7) 55%, rgba(28,33,70,0) 100%),
      linear-gradient(90deg, rgba(255,255,255,1) 0%, rgba(250,244,238,1) 100%);
  }
  .offer-badge {
    position: absolute;
    left: 69px; top: 89px;
    width: 175px; height: 175px;
    background: var(--brand-green);
    border-radius: 8px;
    color: var(--paper);
  }
  .offer-plus {
    position: absolute;
    left: 43px; top: 65px;
    width: 54px; height: 54px;
    background: var(--brand-blue);
    border-radius: 3px;
    z-index: 2;
  }
  .offer-percent {
    position: absolute;
    left: 10px; top: 28px;
    font-weight: 700;
    font-size: 86px;
    line-height: 1;
    letter-spacing: -2px;
  }
  .offer-label {
    position: absolute;
    left: 11px; right: 11px; top: 112px;
    font-weight: 300;
    font-size: 28px;
    line-height: 23px;
  }
  .offer-label span { display: block; }
  .offer-label .second { text-align: right; }
  .headline-box {
    position: absolute;
    left: 257px; top: 90px;
    width: 493px; height: 173px;
    background: var(--brand-blue);
    border-radius: 8px;
    color: var(--paper);
  }
  .headline-kicker {
    position: absolute;
    left: 16px; top: 30px;
    font-weight: 700;
    font-size: 41px;
    line-height: 1;
  }
  .headline-main {
    position: absolute;
    left: 37px; top: 80px;
    font-weight: 700;
    font-size: 72px;
    line-height: 1;
    letter-spacing: -0.5px;
  }
  .brand {
    position: absolute;
    left: 26px; top: 302px;
    display: flex;
    align-items: center;
    color: var(--brand-blue);
  }
  .brand-dot {
    width: 70px; height: 70px;
    border-radius: 50%;
    background: var(--brand-green);
    margin-right: 33px;
  }
  .brand-text { display: flex; flex-direction: column; }
  .brand-service {
    font-weight: 400;
    font-size: 12px;
    line-height: 16px;
    letter-spacing: 0.2px;
  }
  .brand-name {
    font-weight: 700;
    font-size: 40px;
    line-height: 1;
    margin-top: 3px;
    letter-spacing: -0.3px;
  }
  .brand-claim {
    position: absolute;
    left: 346px; top: 338px;
    font-family: "Dancing Script", cursive;
    font-weight: 500;
    font-size: 18px;
    line-height: 17px;
    color: var(--brand-blue);
  }
  .brand-claim span { display: block; }
  .brand-claim .second { padding-left: 18px; }
  .contact-box {
    position: absolute;
    left: 951px; top: 297px;
    width: 221px; height: 75px;
    background: var(--brand-green);
    border-radius: 8px;
    color: var(--paper);
    padding: 8px 0 0 20px;
    font-weight: 500;
    font-size: 17px;
    line-height: 21.5px;
  }
</style>
</head>
<body>
  <div class="banner">
    <div class="photo-child" role="img" aria-label="Foto eines fröhlich tanzenden Mädchens im dunkelblauen Fransen-Partykleid mit Perlenkette"></div>

    <div class="offer-plus">
      <svg width="54" height="54" viewBox="0 0 54 54" aria-hidden="true">
        <path d="M27 13 V41 M13 27 H41" stroke="#ffffff" stroke-width="4" stroke-linecap="square"/>
      </svg>
    </div>
    <div class="offer-badge">
      <div class="offer-percent">20%</div>
      <div class="offer-label"><span>Aktions</span><span class="second">Rabbat</span></div>
    </div>

    <div class="headline-box">
      <div class="headline-kicker">PARTY</div>
      <div class="headline-main">ALLES KLAR!</div>
    </div>

    <div class="brand">
      <div class="brand-dot"></div>
      <div class="brand-text">
        <span class="brand-service">ZENTRALREINIGUNG</span>
        <span class="brand-service">GROSSWÄSCHEREI</span>
        <span class="brand-name">FEINWERK</span>
      </div>
    </div>
    <div class="brand-claim"><span>Wir lieben</span><span class="second">unsere Arbeit</span></div>

    <div class="contact-box">
      LINDENWEG 7<br>
      86999 MUSTERAU,<br>
      TEL.: 01234 - 5678
    </div>
  </div>
</body>
</html>
```